Hualuoya herb bottle label

we need a new label design to reflect our branding for our Chinese herbal medicine product bottles. We import herbs from China and distribute them to Australian Practitioners. The product may be visible to their clients so we want to present it well. Our branding colours and images are attached below, as is the current label layout template. The manufacturer adds the individual names of the herbs and other details over the top so the back ground must be subtle. We would like our name - HuaLuoya at the top to possibly be in yellow/gold and in our chosen font (it will need to be saved and inserted as an image as last print run it reverted to a default font). we would like the blue mountains of the picture below incorporated as the back ground colours. The design needs to feel traditional and artistic. Our name Hualuoya means - essence and spirit. We represent the essence and spirit of traditional Chinese herbal medicine.

```html
<!DOCTYPE html>
<html lang="en">
<head>
<meta charset="utf-8">
<title>Hualuoya herb bottle labels</title>
<link rel="stylesheet" href="https://fonts.googleapis.com/css2?family=Open+Sans:ital,wght@0,400;0,600;0,700;1,600&family=Ma+Shan+Zheng&display=swap">
<style>
  :root {
    --page: #ffffff;
    --ink: #111111;
    --white: #ffffff;
    --blue: #22649a;
    --green: #13855e;
    --gold-dark: #ad763a;
    --gold-mid: #c8914d;
    --gold-light: #f1da92;
    --box-line: #c9c9c9;
    --gold: linear-gradient(90deg, var(--gold-dark) 0%, var(--gold-mid) 14%, var(--gold-light) 34%, var(--gold-mid) 58%, var(--gold-dark) 78%, var(--gold-mid) 100%);
  }
  * { box-sizing: border-box; margin: 0; padding: 0; }
  html, body { width: 1200px; height: 880px; overflow: hidden; background: var(--page); }
  body { position: relative; font-family: "Open Sans", Arial, sans-serif; color: var(--ink); }

  .label {
    position: absolute; top: 90px; width: 438px; height: 701px;
    background: var(--white); overflow: hidden;
    box-shadow: 0 4px 14px rgba(0,0,0,0.12);
  }
  .label--blue { left: 93px; --accent: var(--blue); }
  .label--green { left: 666px; --accent: var(--green); }

  .band { position: absolute; left: 0; width: 100%; }
  .accent { background: var(--accent); }
  .gold { background: var(--gold); }

  .scenery { position: absolute; left: 0; top: 134px; width: 100%; height: 492px; }
  .label--blue .scenery {
    background:
      radial-gradient(ellipse 70% 18% at 75% 60%, rgba(90,140,185,0.45), transparent 70%),
      radial-gradient(ellipse 60% 14% at 25% 55%, rgba(150,185,210,0.4), transparent 70%),
      radial-gradient(ellipse 90% 16% at 50% 95%, rgba(120,160,200,0.45), transparent 70%),
      linear-gradient(180deg, #eef3f8 0%, #f4f7fa 45%, #dfe9f2 75%, #e6eef5 100%);
  }
  .label--green .scenery {
    background:
      radial-gradient(ellipse 40% 30% at 80% 25%, rgba(170,160,145,0.45), transparent 70%),
      radial-gradient(ellipse 45% 25% at 15% 30%, rgba(120,150,125,0.45), transparent 70%),
      radial-gradient(ellipse 80% 25% at 50% 88%, rgba(140,135,120,0.35), transparent 70%),
      linear-gradient(180deg, #e9eeea 0%, #f1f3f1 40%, #dfe7e2 75%, #e5ebe7 100%);
  }

  .brand-band { top: 14px; height: 105px; text-align: center; }
  .brand-name { display: block; font-weight: 700; font-size: 64px; line-height: 1; letter-spacing: 1px; padding-top: 12px; }
  .brand-tagline { display: block; font-weight: 600; font-size: 22px; line-height: 1; margin-top: 5px; }

  .badge {
    position: absolute; left: 158px; top: 128px; width: 122px; height: 193px;
    background: var(--accent); padding: 4px;
  }
  .badge-frame { width: 100%; height: 100%; background: var(--gold); padding: 4px; }
  .badge-inner {
    width: 100%; height: 100%; background: var(--accent);
    display: flex; flex-direction: column; justify-content: center; align-items: center;
    color: var(--white); font-weight: 600; font-size: 32px; line-height: 1.25; letter-spacing: 1px;
  }

  .client-box {
    position: absolute; left: 36px; top: 352px; width: 368px; height: 128px;
    background: var(--white); border: 1.5px solid var(--box-line);
    text-align: center; font-weight: 600; font-size: 27px; line-height: 37px; padding-top: 20px;
  }

  .herb { position: absolute; left: 0; top: 512px; width: 100%; text-align: center; }
  .herb-pinyin { font-weight: 600; font-size: 27px; line-height: 34px; letter-spacing: 0.5px; }
  .herb-latin { font-style: italic; font-weight: 600; font-size: 18px; line-height: 24px; }
  .herb-chinese { font-family: "Ma Shan Zheng", serif; font-size: 38px; line-height: 44px; }

  .weight-band { top: 654px; height: 47px; text-align: center; font-size: 18px; font-weight: 400; line-height: 47px; color: #333; }
</style>
</head>
<body>

<article class="label label--blue">
  <div class="band accent" style="top:0;height:11px"></div>
  <header class="band gold brand-band">
    <span class="brand-name">HUALUOYA</span>
    <span class="brand-tagline">Concentrated Chinese Herbs</span>
  </header>
  <div class="scenery" role="img" aria-label="Soft ink-wash blue mountain landscape with cranes in flight and mist"></div>
  <div class="band accent" style="top:122px;height:12px"></div>
  <div class="band accent" style="top:137px;height:4px"></div>
  <div class="band accent" style="top:144px;height:4px"></div>
  <div class="badge"><div class="badge-frame"><div class="badge-inner"><span>HUA</span><span>LUO</span><span>YA</span></div></div></div>
  <div class="client-box">CLIENT<br>TEXT</div>
  <div class="herb">
    <p class="herb-pinyin">PIAN JIANG HUANG</p>
    <p class="herb-latin">Rhizoma Wenyujin Concisum</p>
    <p class="herb-chinese" lang="zh">片姜黄</p>
  </div>
  <div class="band accent" style="top:623px;height:4px"></div>
  <div class="band accent" style="top:631px;height:4px"></div>
  <div class="band accent" style="top:639px;height:12px"></div>
  <footer class="band gold weight-band">100g NET</footer>
</article>

<article class="label label--green">
  <div class="band accent" style="top:0;height:11px"></div>
  <header class="band gold brand-band">
    <span class="brand-name">HUALUOYA</span>
    <span class="brand-tagline">Concentrated Chinese Herbs</span>
  </header>
  <div class="scenery" role="img" aria-label="Soft watercolour misty green mountain peaks with faint repeating character pattern"></div>
  <div class="band accent" style="top:122px;height:12px"></div>
  <div class="band accent" style="top:137px;height:4px"></div>
  <div class="band accent" style="top:144px;height:4px"></div>
  <div class="badge"><div class="badge-frame"><div class="badge-inner"><span>HUA</span><span>LUO</span><span>YA</span></div></div></div>
  <div class="client-box">CLIENT<br>TEXT</div>
  <div class="herb">
    <p class="herb-pinyin">PIAN JIANG HUANG</p>
    <p class="herb-latin">Rhizoma Wenyujin Concisum</p>
    <p class="herb-chinese" lang="zh">片姜黄</p>
  </div>
  <div class="band accent" style="top:623px;height:4px"></div>
  <div class="band accent" style="top:631px;height:4px"></div>
  <div class="band accent" style="top:639px;height:12px"></div>
  <footer class="band gold weight-band">100g NET</footer>
</article>

</body>
</html>
```